Business Card for new Overseas Property Buying Business

Hi

We need a new business card for our new business.

We are Faraway Nest Seekers. So we search locations on behalf of our clients to find them the ideal home.

These are mainly holiday homes in nice locations - but sometimes people are looking to relocate.

I am looking for a nice simple design - that has some class and professionalism about it. Taking inspiration from our logo.

Text wise I was thinking of maybe having something like. (THE FONT FOR THIS SHOULD BE LIKE THE WRITING IN THE ATTACHMENT WITH THE MAP ON IT)

1)
What does your dream house have (tick all that apply):
swimming pool x
private vineyard x
herb garden x
full sized football pitch x

2)
How to buy a home abroad:

Method 1:
1) Scour internet for suitable estate agents
2) Arrange hectic holiday timetable with multiple agents in multiple languages
3) Fly to destination to find property was not as it seemed
4) Feel frustrated and helpless
OR
Method 2:
Contact your expert home hunter (details overleaf) - and leave the hard work to them

The end result should give people confidence that they are dealing with a professional organisation - and feel like they can place their trust in them. I would want it to drive them to either contact us directly or visit the website.

Please include name (Gordon Marsh), position (founder), contact numbers x 2, email address, website (www.quillan-tarvo.com)

I look forward to seeing your entries.

```html
<!DOCTYPE html>
<html lang="en">
<head>
<meta charset="utf-8">
<title>Faraway Nest Seekers – Business Card</title>
<link rel="stylesheet" href="https://fonts.googleapis.com/css2?family=Shadows+Into+Light+Two&family=Gochi+Hand&display=swap">
<style>
  :root {
    --page: #d4d4d3;
    --card: #eae9e6;
    --ink: #2a2a2a;
    --ink-soft: #5b5b5b;
    --accent: #d2592a;
    --tick: #c8262a;
    --shadow: rgba(0,0,0,0.18);
  }
  * { box-sizing: border-box; margin: 0; padding: 0; }
  html, body { width: 1200px; height: 1200px; overflow: hidden; }
  body {
    background: var(--page);
    font-family: "Shadows Into Light Two", "Gochi Hand", cursive;
    color: var(--ink);
    position: relative;
  }
  .card {
    position: absolute;
    left: 150px;
    width: 900px;
    height: 514px;
    background: var(--card);
    box-shadow: 0 10px 28px var(--shadow);
  }
  .card--front { top: 60px; }
  .card--back  { top: 626px; }

  /* Front */
  .brand {
    position: absolute;
    left: 70px;
    top: 120px;
    width: 340px;
    text-align: center;
  }
  .brand__dot {
    display: block;
    width: 120px;
    height: 120px;
    margin: 0 auto 18px;
    border-radius: 50%;
    background: var(--accent);
  }
  .brand__name {
    font-size: 50px;
    line-height: 1.05;
    color: var(--accent);
  }
  .person {
    position: absolute;
    left: 520px;
    top: 70px;
    width: 330px;
  }
  .person__name {
    font-family: "Gochi Hand", cursive;
    font-size: 52px;
    text-align: center;
    letter-spacing: 1px;
  }
  .person__role {
    font-size: 28px;
    text-align: center;
    color: var(--ink-soft);
    margin-top: -4px;
  }
  .contacts {
    list-style: none;
    margin-top: 60px;
    font-size: 27px;
  }
  .contacts li { line-height: 1.45; white-space: nowrap; }
  .contacts__label {
    display: inline-block;
    width: 78px;
    font-size: 20px;
    color: var(--ink-soft);
  }

  /* Back */
  .wishlist {
    position: absolute;
    left: 60px;
    top: 70px;
    font-size: 27px;
    line-height: 1.3;
  }
  .wishlist__title { margin-bottom: 8px; }
  .wishlist__items { list-style: none; }
  .wishlist__items li { display: flex; align-items: center; justify-content: space-between; width: 370px; }
  .tick-box { width: 26px; height: 26px; flex: none; }

  .howto {
    position: absolute;
    right: 50px;
    top: 40px;
    width: 400px;
    text-align: center;
    font-size: 24px;
    line-height: 1.25;
  }
  .howto__title { font-size: 29px; margin-bottom: 8px; }
  .howto__method { font-family: "Gochi Hand", cursive; font-size: 26px; }
  .howto__steps { list-style: none; }
  .howto__gap { height: 26px; }
</style>
</head>
<body>

<section class="card card--front" aria-label="Business card front">
  <div class="brand">
    <span class="brand__dot"></span>
    <p class="brand__name">Quillan&amp;Tarvo<br>Faraway Nest Seekers</p>
  </div>
  <div class="person">
    <h1 class="person__name">Gordon Marsh</h1>
    <p class="person__role">founder</p>
    <ul class="contacts">
      <li><span class="contacts__label">phone:</span>+012 3 456 789</li>
      <li><span class="contacts__label">phone:</span>+012 3 456 789</li>
      <li><span class="contacts__label">email:</span>quillantarvo@net.com</li>
      <li><span class="contacts__label">web:</span>www.quillan-tarvo.com</li>
    </ul>
  </div>
</section>

<section class="card card--back" aria-label="Business card back">
  <div class="wishlist">
    <p class="wishlist__title">What does your dream house have</p>
    <ul class="wishlist__items">
      <li>swimming pool
        <svg class="tick-box" viewBox="0 0 26 26"><rect x="3" y="3" width="20" height="20" fill="none" stroke="var(--tick)" stroke-width="2.5"/><path d="M6 6 L20 20 M20 6 L6 20" stroke="var(--tick)" stroke-width="2"/></svg></li>
      <li>private vineyard
        <svg class="tick-box" viewBox="0 0 26 26"><rect x="3" y="3" width="20" height="20" fill="none" stroke="var(--tick)" stroke-width="2.5"/><path d="M6 6 L20 20 M20 6 L6 20" stroke="var(--tick)" stroke-width="2"/></svg></li>
      <li>herb garden
        <svg class="tick-box" viewBox="0 0 26 26"><rect x="3" y="3" width="20" height="20" fill="none" stroke="var(--tick)" stroke-width="2.5"/><path d="M6 6 L20 20 M20 6 L6 20" stroke="var(--tick)" stroke-width="2"/></svg></li>
      <li>full sized football pitch
        <svg class="tick-box" viewBox="0 0 26 26"><rect x="3" y="3" width="20" height="20" fill="none" stroke="var(--tick)" stroke-width="2.5"/><path d="M6 6 L20 20 M20 6 L6 20" stroke="var(--tick)" stroke-width="2"/></svg></li>
    </ul>
  </div>

  <div class="howto">
    <p class="howto__title">How to buy a home abroad</p>
    <p class="howto__method">Method 1:</p>
    <ol class="howto__steps">
      <li>1) Scour internet for suitable estate agents</li>
      <li>2) Arrange hectic holiday timetable with multiple agents in multiple languages</li>
      <li>3) Fly to destination to find property was not as it seemed</li>
      <li>4) Feel frustrated and helpless</li>
    </ol>
    <div class="howto__gap"></div>
    <p class="howto__method">Method 2:</p>
    <p>Contact your expert home hunter<br>(details overleaf) -<br>and leave the hard work to them</p>
  </div>
</section>

</body>
</html>
```